Ridgeway Auto Care
Ridgeway Auto Care - Automotive
Creative Brief
Professional
Dale Morrow
President
4817 Silver Fern Ln Braselton,GA 30519
d.morrow@ridgewayautocare.example
www.ridgewayautocare.example

```html
<!DOCTYPE html>
<html lang="en">
<head>
<meta charset="utf-8">
<title>Ridgeway Auto Care – Stationery Set</title>
<link href="https://fonts.googleapis.com/css2?family=Cinzel:wght@600&family=Open+Sans:wght@400;700&display=swap" rel="stylesheet">
<style>
  :root{
    --board:#d45454;
    --board-edge:#c23838;
    --paper:#ffffff;
    --brand-red:#c8161d;
    --deep-red:#8e0f12;
    --slate:#5a5a5c;
    --ink:#3a3a3a;
    --muted:#8a8a8a;
  }
  *{box-sizing:border-box;margin:0;padding:0}
  html,body{width:1200px;height:967px;overflow:hidden}
  body{background:var(--board-edge);font-family:"Open Sans",Arial,sans-serif;color:var(--ink);position:relative}
  .board{position:absolute;left:9px;top:9px;width:1182px;height:949px;background:var(--board)}
  .piece{position:absolute;background:var(--paper);box-shadow:2px 3px 6px rgba(0,0,0,.35);overflow:hidden}
  .piece svg.wave{position:absolute;left:0;bottom:0;width:100%}
  .mark{position:absolute;display:flex;flex-direction:column;align-items:center;gap:3px}
  .mark .dot{border-radius:50%;background:var(--slate)}
  .mark .name{font-family:"Cinzel",Georgia,serif;font-weight:600;color:var(--brand-red);text-align:center;line-height:1.05;letter-spacing:.04em}
  .fine{font-size:4px;line-height:1.5;color:var(--ink);position:absolute}
  .caption{position:absolute;font-size:6px;color:#333}

  .card{width:133px;height:78px}
  .card--red{background:var(--brand-red)}
  .card--slate{background:var(--slate)}
  .card--red .name,.card--slate .name{color:#fff}
  .card--red .dot,.card--slate .dot{background:#d9d9d9}

  .envelope-back{position:absolute;width:210px;height:92px;box-shadow:2px 3px 6px rgba(0,0,0,.35);overflow:hidden;background:#fff}
  .envelope-back .flap{position:absolute;left:0;top:0;width:100%;height:48%}

  .fax h2{font-family:"Open Sans",Arial,sans-serif;font-weight:700;font-size:26px;position:absolute;left:10px;top:32px;color:#111}
  .fax-fields{position:absolute;left:12px;top:74px;width:232px;display:grid;grid-template-columns:1fr 1fr;column-gap:10px;row-gap:4px;font-size:5px}
  .fax-fields span{border-bottom:1px solid #bbb;padding-bottom:1px}
  .fax-checks{position:absolute;left:12px;top:120px;width:232px;display:flex;justify-content:space-between;font-size:4.5px}
  .fax-checks span::before{content:"";display:inline-block;width:4px;height:4px;border:0.6px solid #555;margin-right:2px;vertical-align:middle}
  .fax-rule{position:absolute;left:12px;right:12px;top:132px;border-top:1px solid #444}
</style>
</head>
<body>
<main class="board">

  <!-- Business card front -->
  <section class="piece card" style="left:130px;top:38px">
    <div class="mark" style="left:8px;top:6px">
      <span class="dot" style="width:10px;height:10px"></span>
      <span class="name" style="font-size:5px">Ridgeway<br>Auto Care</span>
    </div>
    <p class="fine" style="left:10px;top:32px">Dale Morrow · President<br>4817 Silver Fern Ln Braselton,GA 30519<br>d.morrow@ridgewayautocare.example</p>
    <svg class="wave" height="30" viewBox="0 0 100 100" preserveAspectRatio="none"><path d="M0 70 C35 20 65 110 100 10 L100 100 L0 100Z" fill="var(--brand-red)"/><path d="M0 85 C35 40 65 120 100 35 L100 100 L0 100Z" fill="#fff"/></svg>
  </section>

  <!-- Business card back red -->
  <section class="piece card card--red" style="left:130px;top:166px">
    <div class="mark" style="left:0;right:0;top:18px">
      <span class="dot" style="width:14px;height:14px"></span>
      <span class="name" style="font-size:10px">Ridgeway Auto Care</span>
    </div>
  </section>

  <!-- Business card back slate -->
  <section class="piece card card--slate" style="left:130px;top:286px">
    <div class="mark" style="left:0;right:0;top:18px">
      <span class="dot" style="width:14px;height:14px"></span>
      <span class="name" style="font-size:10px">Ridgeway Auto Care</span>
    </div>
  </section>

  <!-- Letterhead -->
  <section class="piece" style="left:315px;top:43px;width:241px;height:332px">
    <div class="mark" style="left:10px;top:10px">
      <span class="dot" style="width:12px;height:12px"></span>
      <span class="name" style="font-size:6px">Ridgeway<br>Auto Care</span>
    </div>
    <p class="fine" style="left:10px;top:300px">4817 Silver Fern Ln Braselton,GA 30519<br>www.ridgewayautocare.example</p>
    <svg class="wave" height="40" viewBox="0 0 100 100" preserveAspectRatio="none"><path d="M0 60 C30 10 60 110 100 0 L100 100 L0 100Z" fill="var(--brand-red)"/><path d="M0 75 C30 30 60 120 100 25 L100 100 L0 100Z" fill="#fff"/></svg>
  </section>

  <!-- Compliment square -->
  <section class="piece" style="left:605px;top:43px;width:71px;height:66px">
    <div class="mark" style="left:0;right:0;top:6px">
      <span class="dot" style="width:9px;height:9px"></span>
      <span class="name" style="font-size:4.5px">Ridgeway<br>Auto Care</span>
    </div>
    <svg class="wave" height="18" viewBox="0 0 100 100" preserveAspectRatio="none"><path d="M0 60 C30 10 60 110 100 0 L100 100 L0 100Z" fill="var(--brand-red)"/><path d="M0 80 C30 35 60 120 100 30 L100 100 L0 100Z" fill="#fff"/></svg>
  </section>

  <!-- Address label -->
  <section class="piece" style="left:605px;top:184px;width:73px;height:58px">
    <div class="mark" style="left:5px;top:5px">
      <span class="dot" style="width:7px;height:7px"></span>
      <span class="name" style="font-size:4px">Ridgeway<br>Auto Care</span>
    </div>
    <svg class="wave" height="18" viewBox="0 0 100 100" preserveAspectRatio="none"><path d="M0 60 C30 10 60 110 100 0 L100 100 L0 100Z" fill="var(--brand-red)"/><path d="M0 80 C30 35 60 120 100 30 L100 100 L0 100Z" fill="#fff"/></svg>
  </section>

  <!-- Strip label -->
  <section class="piece" style="left:605px;top:252px;width:73px;height:34px">
    <svg class="wave" height="12" viewBox="0 0 100 100" preserveAspectRatio="none"><path d="M0 60 C30 10 60 110 100 0 L100 100 L0 100Z" fill="var(--brand-red)"/><path d="M0 80 C30 35 60 120 100 30 L100 100 L0 100Z" fill="#fff"/></svg>
  </section>

  <!-- DL envelope front -->
  <section class="piece" style="left:605px;top:292px;width:218px;height:95px">
    <div class="mark" style="left:8px;top:6px">
      <span class="dot" style="width:9px;height:9px"></span>
      <span class="name" style="font-size:4.5px">Ridgeway<br>Auto Care</span>
    </div>
    <svg class="wave" height="26" viewBox="0 0 100 100" preserveAspectRatio="none"><path d="M0 60 C30 10 60 110 100 0 L100 100 L0 100Z" fill="var(--brand-red)"/><path d="M0 80 C30 35 60 120 100 30 L100 100 L0 100Z" fill="#fff"/></svg>
  </section>

  <!-- Envelope backs -->
  <section class="envelope-back" style="left:897px;top:300px">
    <svg class="flap" viewBox="0 0 100 100" preserveAspectRatio="none"><path d="M0 0 H100 V100 H0Z" fill="var(--deep-red)"/></svg>
  </section>
  <section class="envelope-back" style="left:905px;top:326px">
    <svg class="flap" viewBox="0 0 100 100" preserveAspectRatio="none"><path d="M0 0 H100 V100 H0Z" fill="var(--brand-red)"/></svg>
  </section>
  <section class="envelope-back" style="left:913px;top:352px">
    <svg class="flap" viewBox="0 0 100 100" preserveAspectRatio="none"><path d="M0 0 H100 V100 H0Z" fill="var(--slate)"/></svg>
  </section>
  <p class="caption" style="left:990px;top:452px">Envelope Back</p>

  <!-- Presentation folder -->
  <section class="piece" style="left:130px;top:448px;width:466px;height:432px;background:var(--slate)">
    <svg style="position:absolute;left:0;top:0" width="466" height="432" viewBox="0 0 466 432" preserveAspectRatio="none">
      <path d="M0 0 H466 V250 C360 210 250 310 130 270 C80 254 40 250 0 262Z" fill="#fff"/>
      <path d="M0 262 C40 250 80 254 130 270 C250 310 360 210 466 250 V262 C360 224 250 324 130 284 C80 268 40 264 0 276Z" fill="var(--brand-red)"/>
      <path d="M0 250 C40 238 80 242 130 258 C250 298 360 198 466 238 V250 C360 210 250 310 130 270 C80 254 40 250 0 262Z" fill="var(--deep-red)" opacity=".35"/>
    </svg>
    <div class="mark" style="left:0;top:22px;width:96px">
      <span class="dot" style="width:28px;height:28px"></span>
      <span class="name" style="font-size:9px">Ridgeway<br>Auto Care</span>
    </div>
    <div class="piece card" style="left:175px;top:340px;width:56px;height:34px;box-shadow:1px 1px 3px rgba(0,0,0,.4)"></div>
  </section>
  <p class="caption" style="left:330px;top:884px">Presentation Folder</p>

  <!-- CD sleeve -->
  <section class="piece" style="left:622px;top:562px;width:162px;height:256px">
    <div class="mark" style="left:0;right:0;top:62px">
      <span class="dot" style="width:34px;height:34px"></span>
      <span class="name" style="font-size:10px">Ridgeway<br>Auto Care</span>
    </div>
    <svg class="wave" height="70" viewBox="0 0 100 100" preserveAspectRatio="none"><path d="M0 40 C30 0 60 70 100 10 L100 100 L0 100Z" fill="var(--brand-red)"/><path d="M0 55 C30 15 60 85 100 25 L100 100 L0 100Z" fill="var(--slate)"/></svg>
  </section>

  <!-- CD disc -->
  <svg style="position:absolute;left:635px;top:471px;filter:drop-shadow(2px 3px 3px rgba(0,0,0,.35))" width="132" height="132" viewBox="0 0 132 132">
    <defs><clipPath id="disc"><circle cx="66" cy="66" r="64"/></clipPath></defs>
    <g clip-path="url(#disc)">
      <rect width="132" height="132" fill="#fff"/>
      <path d="M0 70 C40 50 80 100 132 60 V132 H0Z" fill="var(--brand-red)"/>
      <path d="M0 78 C40 58 80 108 132 68 V132 H0Z" fill="var(--slate)"/>
    </g>
    <circle cx="66" cy="66" r="9" fill="var(--board)"/>
    <circle cx="66" cy="34" r="7" fill="var(--slate)"/>
  </svg>

  <!-- Fax sheet -->
  <section class="piece fax" style="left:822px;top:484px;width:256px;height:347px">
    <div class="mark" style="left:10px;top:6px;flex-direction:row;gap:4px">
      <span class="dot" style="width:9px;height:9px"></span>
      <span class="name" style="font-size:5px">Ridgeway Auto Care</span>
    </div>
    <h2>Fax</h2>
    <div class="fax-fields">
      <span>To:</span><span>From:</span>
      <span>Fax:</span><span>Phone:</span>
      <span>Date:</span><span>Re:</span>
      <span>Pages:</span><span>CC:</span>
    </div>
    <div class="fax-checks"><span>Urgent</span><span>For Review</span><span>Please Comment</span><span>Please Recycle</span></div>
    <div class="fax-rule"></div>
    <p class="fine" style="left:12px;top:316px">4817 Silver Fern Ln Braselton,GA 30519<br>www.ridgewayautocare.example</p>
    <svg class="wave" height="22" viewBox="0 0 100 100" preserveAspectRatio="none"><path d="M0 60 C30 10 60 110 100 0 L100 100 L0 100Z" fill="var(--brand-red)"/><path d="M0 80 C30 35 60 120 100 30 L100 100 L0 100Z" fill="#fff"/></svg>
  </section>

</main>
</body>
</html>
```